Varindel Homes needs a stationery design

I need a stationary design for my new custom home building company. Our company deals with very high end and luxurious homes so i need a stationary design that shows strength, elegance, and trust.
The final version should be trendy, clean... only 2 colours (green + grey/black) and professional.
#1: Business Cards (design on 2 sides)
#2: Letterhead (word format)
#3: Cover Page and back cover for proposals
#4: Envelopes,
#5: Thank You card,
#6: Presentation Folder
Logo is attached. Logo can be reversed out (will attach once available). Logo can be stacked or horizontal (provided as horizontal).
The business cards need to be two sided with the company logo and website on the front (www.varindelhomes-demo.net and contact info on the back.
The contact info can be made up temporarily and once the final design is chosen, i will provide you with all the correct contact information during the revision stage.
id like to see examples with black, white, blue, red, purple. (You should not try to use all these in one design)
I have attached my company's logo in 3 different colours and a few sample business cards that i found on the internet. I would like to see unique designs though, don't try to imitate the examples
Updates
Dear designers,
I have also attached the .eps and ai files for the 3 different coloured logos.
Please notify me if you need anything else to complete your work
Best Regards,
Varindel

```html
<!DOCTYPE html>
<html lang="en">
<head>
<meta charset="utf-8">
<title>Varindel Homes – Stationery Set</title>
<link href="https://fonts.googleapis.com/css2?family=Arimo:wght@400;700&display=swap" rel="stylesheet">
<style>
  :root{
    --bg:#1d1d1d;
    --paper:#ffffff;
    --ink:#3a3a3a;
    --muted:#8a8a8a;
    --blue:#1565c8;
    --blue-light:#22a0e6;
    --blue-dark:#0a2c86;
    --charcoal:#232323;
    --swoosh:#eeeeee;
  }
  *{box-sizing:border-box;margin:0;padding:0}
  html,body{width:1200px;height:1000px;overflow:hidden;background:var(--bg);font-family:"Arimo",Arial,sans-serif;color:var(--ink)}
  .canvas{position:relative;width:1200px;height:1000px}
  .sheet{position:absolute;overflow:hidden;box-shadow:0 10px 24px rgba(0,0,0,.5)}
  .sheet > svg.shapes{position:absolute;inset:0;width:100%;height:100%}
  .brand-name{position:absolute;font-weight:700;letter-spacing:.04em;text-transform:uppercase;white-space:nowrap}
  .brand-mark{display:inline-block;width:.7em;height:.7em;margin-right:.35em;vertical-align:baseline}
  .on-white .brand-name{color:var(--blue)}
  .on-white .brand-mark{background:var(--blue)}
  .on-blue .brand-name{color:#fff}
  .on-blue .brand-mark{background:#fff}

  /* Letterhead */
  .letterhead{width:368px;height:520px;top:240px}
  .letterhead-back{left:40px;background:var(--paper)}
  .letterhead-front{left:430px;background:var(--paper)}
  .letterhead .brand-name{font-size:15px}
  .letterhead-front .brand-name{top:26px;left:0;right:0;text-align:center}
  .letterhead-back .brand-name{top:38px;left:32px}
  .letter-body{position:absolute;top:78px;left:32px;right:32px;font-size:6.6px;line-height:1.75;color:var(--ink)}
  .letter-body p{margin-bottom:9px}
  .signature{position:absolute;top:290px;right:36px;width:110px;text-align:center}
  .signature-ink{height:26px;background:#f1f1f1;border-bottom:1px solid #bbb}
  .signature-name{font-size:6px;letter-spacing:.06em;margin-top:3px;color:var(--muted)}
  .footer-address{position:absolute;right:10px;top:442px;color:#fff;font-size:6.4px;line-height:1.35}
  .footer-address .ico{display:inline-block;width:6px;height:6px;background:#fff;margin-right:4px;vertical-align:middle}
  .footer-web{position:absolute;left:14px;top:480px;font-size:8px;color:var(--blue-dark)}
  .footer-web .ico,.footer-phone .ico{display:inline-block;width:7px;height:7px;border:1px solid currentColor;border-radius:50%;margin-right:5px;vertical-align:middle}
  .footer-phone{position:absolute;left:14px;top:503px;font-size:7.4px;color:#fff}

  /* Business cards */
  .card{width:160px;height:92px;top:240px}
  .card-front{left:830px;background:var(--paper)}
  .card-back{left:1000px}
  .card-front .brand-name{font-size:6px;letter-spacing:.02em;top:14px;left:10px}
  .card-person{position:absolute;left:10px;top:50px}
  .card-person .name{font-size:7.5px;font-weight:700;color:var(--ink)}
  .card-person .role{font-size:5px;color:var(--muted);margin-top:2px}
  .card-contacts{position:absolute;left:80px;top:12px;font-size:4.2px;line-height:1.6;color:var(--ink);border-left:1.5px solid var(--blue-dark);padding-left:5px;white-space:nowrap}
  .card-back .brand-name{font-size:10px;top:32px;left:0;right:0;text-align:center}
  .card-back .site{position:absolute;bottom:10px;right:10px;font-size:4.6px;color:#d6e6ff}

  /* Envelopes */
  .envelope{width:330px;height:165px;left:830px}
  .envelope-front{top:352px;background:var(--paper)}
  .envelope-back{top:540px}
  .envelope-front .brand-name{font-size:14px;top:30px;left:18px}
  .envelope-contacts{position:absolute;left:26px;top:62px;font-size:7px;line-height:1.45;border-left:2px solid var(--blue-dark);padding-left:8px;color:var(--ink)}
  .envelope-back .brand-name{font-size:13px;top:34px;left:0;right:0;text-align:center}
  .envelope-back .site{position:absolute;right:22px;bottom:22px;font-size:7px;color:#d6e6ff}
</style>
</head>
<body>
<main class="canvas">

  <section class="sheet letterhead letterhead-back on-blue" aria-label="Letterhead reverse">
    <svg class="shapes" viewBox="0 0 368 520" preserveAspectRatio="none" aria-hidden="true">
      <defs>
        <linearGradient id="lhBack" x1="0" y1="0" x2="0.6" y2="1">
          <stop offset="0" stop-color="var(--blue-light)"/>
          <stop offset="1" stop-color="var(--blue-dark)"/>
        </linearGradient>
      </defs>
      <rect width="368" height="470" fill="url(#lhBack)"/>
      <path d="M0 20 Q120 -5 368 12 L368 0 L0 0Z" fill="#fff" opacity=".12"/>
      <polygon points="240,432 368,432 368,470 218,470" fill="var(--paper)"/>
      <polygon points="0,470 368,470 368,520 0,520" fill="var(--paper)"/>
      <polygon points="0,500 368,498 368,520 0,520" fill="var(--blue)"/>
      <polygon points="250,470 368,470 368,476 244,476" fill="var(--charcoal)"/>
    </svg>
    <div class="brand-name"><span class="brand-mark"></span>Varindel Homes</div>
    <div class="footer-address" style="color:var(--blue-dark)"><span class="ico" style="background:var(--blue-dark)"></span>Varindel Homes Street<br>&nbsp;&nbsp;&nbsp;Varindel Homes Street, 01234</div>
    <div class="footer-web"><span class="ico"></span>hello@varindelhomes-demo.net | www.varindelhomes-demo.net</div>
    <div class="footer-phone"><span class="ico"></span>Tel. +012 555 0142 | Fax +012 555 0142 | Mobile +012 555 0142</div>
  </section>

  <section class="sheet letterhead letterhead-front on-white" aria-label="Letterhead">
    <svg class="shapes" viewBox="0 0 368 520" preserveAspectRatio="none" aria-hidden="true">
      <path d="M0 40 Q90 10 200 0 L0 0Z" fill="var(--swoosh)"/>
      <path d="M0 70 Q60 30 150 0 L120 0 Q40 30 0 55Z" fill="#f5f5f5"/>
      <polygon points="110,0 368,0 368,12" fill="var(--blue)"/>
      <polygon points="230,0 368,0 368,5" fill="var(--blue-dark)"/>
      <polygon points="246,432 368,432 368,470 222,470" fill="var(--charcoal)"/>
      <polygon points="0,470 368,470 368,474 0,476" fill="var(--blue-dark)"/>
      <polygon points="0,498 368,496 368,520 0,520" fill="var(--blue)"/>
    </svg>
    <div class="brand-name"><span class="brand-mark"></span>Varindel Homes</div>
    <div class="letter-body">
      <p>Lorem ipsum is simply dummy text of the printing and typesetting industry. It has been the standard dummy text ever since the early days, when a printer took a galley of type and scrambled it to make a specimen book. It has survived many decades and remains essentially unchanged today.</p>
      <p>It is a long established fact that a reader will be distracted by the readable content of a page when looking at its layout, as opposed to using plain content here.</p>
      <p>Many desktop publishing packages and web page editors now use this text as their default model, and a search will uncover many web sites still in their infancy.</p>
    </div>
    <div class="signature">
      <div class="signature-ink" role="img" aria-label="Handwritten signature"></div>
      <div class="signature-name">TOBIAS RENNER</div>
    </div>
    <div class="footer-address"><span class="ico"></span>Varindel Homes Street<br>&nbsp;&nbsp;&nbsp;Varindel Homes Street, 01234</div>
    <div class="footer-web"><span class="ico"></span>hello@varindelhomes-demo.net | www.varindelhomes-demo.net</div>
    <div class="footer-phone"><span class="ico"></span>Tel. +012 555 0142 | Fax +012 555 0142 | Mobile +012 555 0142</div>
  </section>

  <section class="sheet card card-front on-white" aria-label="Business card front">
    <svg class="shapes" viewBox="0 0 160 92" preserveAspectRatio="none" aria-hidden="true">
      <path d="M0 30 Q50 8 110 0 L0 0Z" fill="var(--swoosh)"/>
      <polygon points="100,76 160,72 160,92 96,92" fill="var(--charcoal)"/>
      <polygon points="0,84 160,82 160,92 0,92" fill="var(--blue)"/>
    </svg>
    <div class="brand-name"><span class="brand-mark"></span>Varindel Homes</div>
    <div class="card-person">
      <div class="name">MAREK DALTON</div>
      <div class="role">Managing director</div>
    </div>
    <div class="card-contacts">
      Varindel Homes Street<br>
      Varindel Homes Street, 01234<br>
      hello@varindelhomes-demo.net<br>
      www.varindelhomes-demo.net<br>
      Tel. +012 555 0142<br>
      Fax +012 555 0142
    </div>
  </section>

  <section class="sheet card card-back on-blue" aria-label="Business card back">
    <svg class="shapes" viewBox="0 0 160 92" preserveAspectRatio="none" aria-hidden="true">
      <defs>
        <linearGradient id="cardBack" x1="0" y1="0" x2="1" y2="1">
          <stop offset="0" stop-color="var(--blue-light)"/>
          <stop offset="1" stop-color="var(--blue-dark)"/>
        </linearGradient>
      </defs>
      <rect width="160" height="92" fill="url(#cardBack)"/>
      <path d="M0 18 Q70 2 160 10 L160 0 L0 0Z" fill="#fff" opacity=".12"/>
    </svg>
    <div class="brand-name"><span class="brand-mark"></span>Varindel Homes</div>
    <div class="site">www.varindelhomes-demo.net</div>
  </section>

  <section class="sheet envelope envelope-front on-white" aria-label="Envelope front">
    <svg class="shapes" viewBox="0 0 330 165" preserveAspectRatio="none" aria-hidden="true">
      <path d="M0 50 Q140 10 330 30 L330 0 L0 0Z" fill="var(--swoosh)"/>
      <path d="M80 0 Q200 40 330 48 L330 38 Q210 30 110 0Z" fill="#f4f4f4"/>
      <polygon points="232,120 330,106 330,140 222,140" fill="var(--charcoal)"/>
      <polygon points="0,140 330,138 330,165 0,165" fill="var(--blue)"/>
      <polygon points="0,140 330,138 330,142 0,145" fill="var(--blue-dark)"/>
    </svg>
    <div class="brand-name"><span class="brand-mark"></span>Varindel Homes</div>
    <div class="envelope-contacts">
      Varindel Homes Street<br>
      Varindel Homes Street, 01234<br>
      hello@varindelhomes-demo.net<br>
      www.varindelhomes-demo.net<br>
      Tel. +012 555 0142 · Fax +012 555 0142
    </div>
  </section>

  <section class="sheet envelope envelope-back on-blue" aria-label="Envelope back">
    <svg class="shapes" viewBox="0 0 330 165" preserveAspectRatio="none" aria-hidden="true">
      <defs>
        <linearGradient id="envBack" x1="0" y1="0" x2="1" y2="1">
          <stop offset="0" stop-color="var(--blue-light)"/>
          <stop offset="1" stop-color="var(--blue-dark)"/>
        </linearGradient>
      </defs>
      <rect width="330" height="165" fill="url(#envBack)"/>
      <polyline points="0,0 70,70 260,70 330,0" fill="none" stroke="#fff" stroke-opacity=".18" stroke-width="1"/>
      <polygon points="0,150 330,146 330,165 0,165" fill="var(--blue-light)" opacity=".55"/>
    </svg>
    <div class="brand-name"><span class="brand-mark"></span>Varindel Homes</div>
    <div class="site">www.varindelhomes-demo.net</div>
  </section>

</main>
</body>
</html>
```